Smart, Classy, Conservative looking Legal Letterhead

I need a letterhead that when you look at it it "says to you " this is a well established law firm with very smart lawyers, which will one day be appearing before the Supreme Court of the USA. All information about the Law firm should appear at the top of the page. please no information in the footer.

Industry/Entity Type

Legal

Requirements
Must have
• The name of the law firm, both addresses, phone number and fax,, The names of the attorneys, the website.
• Fields that get changed such as the date, VIA, Address of who the letter is going to,
• Re, Index,
• should have a clean neat look, sleek
Nice to have
• some color would be nice. A logo of some sort could be nice as well. Maybe a single S or interlocking P's For Pelworth and Pelworth.
Should not have
• not too modern looking.

```html
<!DOCTYPE html>
<html lang="en">
<head>
<meta charset="utf-8">
<title>Pelworth &amp; Pelworth Letterhead</title>
<link rel="stylesheet" href="https://fonts.googleapis.com/css2?family=Libre+Baskerville:ital,wght@0,400;0,700;1,400&display=swap">
<style>
  :root {
    --backdrop: #e6e3de;
    --paper: #ffffff;
    --ink: #1d1b18;
    --ink-soft: #4a4640;
    --gold-deep: #a8820c;
    --gold-bright: #d6b222;
    --gold-faint: rgba(214, 178, 34, 0.12);
  }
  * { margin: 0; padding: 0; box-sizing: border-box; }
  html, body {
    width: 1200px; height: 700px; overflow: hidden;
    background: var(--backdrop);
    font-family: "Libre Baskerville", "Times New Roman", serif;
    color: var(--ink);
  }
  .letterhead {
    position: absolute; left: 352px; top: 30px;
    width: 495px; height: 640px;
    background: var(--paper);
    box-shadow: 0 2px 10px rgba(0,0,0,0.12);
    overflow: hidden;
  }
  .watermark {
    position: absolute; left: 0; right: 0; top: 250px;
    text-align: center;
    font-size: 76px; font-weight: 700; line-height: 1;
    color: var(--gold-faint);
    white-space: nowrap;
  }
  .firm-mark {
    position: absolute; left: 30px; top: 30px;
    font-size: 13px; font-weight: 700; color: var(--gold-deep);
  }
  .firm-header {
    position: absolute; left: 0; right: 0; top: 28px;
    text-align: center;
  }
  .firm-name { font-size: 17px; font-weight: 700; letter-spacing: 0.5px; }
  .firm-tagline { font-size: 10px; font-weight: 700; letter-spacing: 1.5px; margin-top: 3px; }
  .firm-contact { font-size: 6.5px; line-height: 1.5; margin-top: 5px; color: var(--ink-soft); }
  .letter-date { font-size: 9px; margin-top: 8px; }
  .attorney-list {
    position: absolute; right: 26px; top: 30px;
    list-style: none; text-align: right;
    font-size: 6.5px; font-weight: 700; line-height: 1.6;
  }
  .recipient {
    position: absolute; left: 30px; top: 150px;
    font-size: 6.5px; line-height: 1.55; font-style: normal;
  }
  .recipient .delivery { font-weight: 700; }
  .matter {
    position: absolute; left: 200px; top: 150px; right: 26px;
    font-size: 6.5px; line-height: 1.55;
  }
  .matter b { font-weight: 700; }
  .letter-body {
    position: absolute; left: 30px; right: 40px; top: 225px;
    font-size: 6.5px; line-height: 1.6;
  }
  .letter-body p { margin-bottom: 9px; }
  .letter-body .indent { text-indent: 40px; }
  .signature { margin-top: 4px; }
  .footer-band {
    position: absolute; left: 0; right: 0; bottom: 0; height: 60px;
    background: linear-gradient(90deg, var(--gold-deep), var(--gold-bright) 60%, var(--gold-deep));
    color: #fff;
  }
  .footer-band .cc {
    position: absolute; left: 30px; bottom: 12px; font-size: 7px;
  }
  .footer-band .band-mark {
    position: absolute; right: 22px; top: 12px;
    font-size: 9px; font-weight: 700;
  }
</style>
</head>
<body>
  <main class="letterhead">
    <div class="watermark" aria-hidden="true">Pelworth</div>

    <div class="firm-mark">Pelworth</div>

    <header class="firm-header">
      <h1 class="firm-name">PELWORTH &amp; PELWORTH</h1>
      <p class="firm-tagline">ATTORNEYS AT LAW</p>
      <p class="firm-contact">
        418 Garrison Avenue, Suite 12<br>
        Albany, NY 12207<br>
        Tel 518.555.0142 &middot; Fax 518.555.0143<br>
        www.pelworthlaw.com
      </p>
      <p class="letter-date">July 1st 2015</p>
    </header>

    <ul class="attorney-list">
      <li>Daniel A. Pelworth</li>
      <li>Miriam T. Hale</li>
      <li>Jonas R. Whitcombe</li>
      <li>Clara E. Voss</li>
      <li>Simon L. Garner</li>
    </ul>

    <address class="recipient">
      <span class="delivery">VIA COURIER</span><br>
      Hon. Judge Eleanor Marsh<br>
      Harlow County Superior Court<br>
      40 Linden Row, Room 7<br>
      Easton Falls, NY 12900
    </address>

    <div class="matter">
      <p><b>Re:</b> XXXXXXXXXXXXXXXXXXXXXXXXXXXXXXXX</p>
      <p><b>Index:</b> XXXXXXXXXXXXXXXXXXXXXXXXXXXX</p>
    </div>

    <section class="letter-body">
      <p>Your Honor,</p>
      <p class="indent">Pursuant to Your Honor's Individual Rules, we write on behalf of our client to request a brief adjournment of the conference scheduled for next month.</p>
      <p class="indent">Opposing counsel consents to this request, and no prior adjournment has been sought. We thank the Court for its time and consideration.</p>
      <p class="indent">Should the Court require anything further, we remain available at its convenience.</p>
      <p class="signature">Respectfully,<br>Daniel A. Pelworth</p>
    </section>

    <footer class="footer-band">
      <span class="band-mark">Pelworth</span>
      <p class="cc">CC: Enter opposing counsel name here</p>
    </footer>
  </main>
</body>
</html>
```